Flyer-Design für Immobilienfirma
Zielgruppe
www.brenkholt-immobilien.de
Aufgabenstellung
Thema :
Neukunden generieren – Viele Wege führen zu neuen Leads ...
Sich selbst als Experten platzieren mit Bild
Dienstleistung : FÜR DEN IMMOBILIENBESITZER
Was ist Ihre Immobilie wert?
KOSTENLOSE Beratung durch Experten
KOSTENLOSE Immobilienbewertung
KOSTENLOS vorhandene Grundrisszeichnungen aktualisieren
KOSTENLOS 3D Grundrisszeichnungen und Ansicht
KOSTENLOS 3D Fotos und 360 Grad Ansichten
KOSTENLOS Drohnenaufnahmen IHRER Immobilien
KOSTENLOS Erstellung eines Energieverbrauchsausweises
evtl für die Rückseite
#Tippgeberprämie
Brenkholt & Partner Immobilien
so einfach verdienen Sie sich Ihre Tippprämie
wenn Sie Kenntnis vom beabsichtigten Verkauf einer Immobilie haben, dann setzen Sie sich mit uns in Verbindung.
Wir belohnen Ihren Tipp – wenn er zu einem Verkaufsabschluss durch uns führt –
mit 10 Prozent der an uns gezahlten Netto-Vermittlungsprovision (ohne MwSt.).
Dies gilt auch für Eigentümer, die uns Ihre Immobilie zum Verkauf geben.
Voraussetzungen für die Zahlung einer Tippgeber-Prämie sind:
Die Brenkholt & Partner immobilien kennt das angebotene Objekt noch nicht.
Das Objekt wird nicht bereits im Internet von dritter Seite beworben.
Die Brenkholt & Partner immobilien erhält die Erlaubnis zur Vermarktung der Immobilie.
Es kommt zu einem durch die Brenkholt & Partner immobilien vermittelten Verkauf
Sie erhalten Ihre Tippprämie unmittelbar nach Zahlung der Courtage an uns auf ein von Ihnen genanntes Konto überwiesen!

```html
<!DOCTYPE html>
<html lang="de">
<head>
<meta charset="utf-8">
<title>Brenkholt &amp; Partner – Flyer</title>
<link rel="stylesheet" href="https://fonts.googleapis.com/css2?family=Quicksand:wght@400;500;600;700&display=swap">
<style>
:root{
  --brown:#4a3a28;
  --brown-dark:#3b2e20;
  --gold:#d9a02a;
  --ink:#3a3025;
  --paper:#ffffff;
  --canvas:#e4e4e4;
  --divider:#d8d0c4;
}
*{box-sizing:border-box;margin:0;padding:0}
html,body{width:1200px;height:2400px;overflow:hidden}
body{background:var(--canvas);font-family:"Quicksand",sans-serif;color:var(--ink);position:relative}
.flyer{position:absolute;left:210px;width:780px;height:1103px;background:var(--paper);overflow:hidden;box-shadow:0 10px 30px rgba(0,0,0,.18)}
.flyer--front{top:64px}
.flyer--back{top:1233px}
.shapes{position:absolute;inset:0;width:780px;height:1103px}
.abs{position:absolute}

/* front top */
.brand-panel{left:0;top:0;width:310px;height:400px;background:var(--brown)}
.portrait{left:310px;top:0;width:470px;height:480px;background:linear-gradient(110deg,#cfd9e2 0%,#b9c4cc 30%,#c79a63 60%,#a9743f 100%)}
.brand-name{left:60px;top:48px;font-size:34px;font-weight:700;color:#fff;letter-spacing:.5px}
.brand-sub{left:120px;top:92px;font-size:13px;color:#fff;font-weight:500}
.claim-box{left:48px;top:140px;width:214px;height:120px;border:2px solid var(--gold);display:flex;align-items:center;justify-content:center;text-align:center;color:#fff;font-weight:700;font-size:19px;line-height:1.25}
.url-band{left:48px;top:272px;width:214px;height:26px;background:var(--gold);color:var(--brown-dark);font-size:12px;font-weight:700;display:flex;align-items:center;justify-content:center}
.name-tag{left:500px;top:300px;width:280px;height:36px;background:var(--gold);color:#fff;font-weight:700;font-size:20px;padding-left:18px;line-height:36px}
.role-tag{left:530px;top:336px;width:250px;height:34px;background:var(--brown-dark);color:#fff;font-weight:700;font-size:18px;padding-left:18px;line-height:34px}

.headline{left:0;width:780px;text-align:center;font-weight:700;color:var(--ink);font-size:36px;letter-spacing:.5px}
.subline{left:0;width:780px;text-align:center;color:var(--gold);font-size:22px;font-weight:500;letter-spacing:1px}
.subline span{display:inline-block;padding:0 14px;position:relative}
.subline span::before,.subline span::after{content:"";position:absolute;top:50%;width:90px;height:2px;background:var(--gold)}
.subline span::before{right:100%}.subline span::after{left:100%}

.service{position:absolute;display:flex;align-items:flex-start;gap:16px;width:320px}
.service .icon{flex:0 0 58px;height:58px;border:2px solid var(--gold);border-radius:50%;display:flex;align-items:center;justify-content:center}
.service .icon svg{width:30px;height:30px}
.service h3{color:var(--gold);font-size:17px;font-weight:700;letter-spacing:.5px}
.service p{font-size:17px;line-height:1.2;color:var(--ink);font-weight:500}
.col-divider{left:395px;top:620px;width:2px;height:250px;background:var(--divider);transform:rotate(12deg)}

/* footer */
.contact{position:absolute;color:#fff;font-size:13px;line-height:1.3;display:flex;gap:8px;align-items:flex-start}
.contact svg{flex:0 0 18px;width:18px;height:18px;margin-top:2px}
.contact b{font-weight:700}
.footer-url{color:#fff;font-size:13px;font-weight:700}

/* back */
.street{left:0;top:0;width:780px;height:400px;background:linear-gradient(180deg,#a9c3de 0%,#c9cfc6 35%,#6f7a4e 55%,#8a7a66 80%,#5c5248 100%)}
.phone-tag{left:520px;top:80px;width:260px;height:40px;background:var(--gold);color:#fff;font-weight:700;font-size:20px;display:flex;align-items:center;gap:12px;padding-left:14px}
.phone-tag .dot{width:28px;height:28px;border-radius:50%;background:var(--brown-dark);display:flex;align-items:center;justify-content:center}
.phone-tag svg{width:16px;height:16px}
.band-title{left:0;top:410px;width:780px;text-align:center;color:#fff;font-weight:700;font-size:40px;letter-spacing:1px}
.band-sub{left:0;top:462px;width:780px;text-align:center;color:var(--gold);font-size:18px;font-weight:500;letter-spacing:1px}
.tip-text{left:60px;top:560px;width:660px;font-size:15px;line-height:1.4;font-weight:500}
.tip-text p{margin-bottom:8px}
.tip-text strong{font-weight:700}
.tip-list{list-style:none}
.tip-list li{position:relative;padding-left:24px;margin-bottom:4px}
.tip-list li::before{content:"";position:absolute;left:0;top:4px;width:14px;height:14px;border-radius:50%;background:var(--gold)}
.tip-list li::after{content:"";position:absolute;left:4px;top:7px;width:5px;height:3px;border-left:2px solid #fff;border-bottom:2px solid #fff;transform:rotate(-45deg)}
</style>
</head>
<body>

<section class="flyer flyer--front">
  <div class="abs brand-panel"></div>
  <div class="abs portrait" role="img" aria-label="Porträtfoto des Geschäftsführers vor einer Holzwand"></div>
  <div class="abs brand-name">Brenkholt</div>
  <div class="abs brand-sub">&amp; Partner Real Estate</div>
  <div class="abs claim-box">SERVICE.<br>QUALITÄT.<br>FLEXIBILITÄT.</div>
  <div class="abs url-band">www.brenkholt-immobilien.de</div>
  <div class="abs name-tag">Henrik Brenkholt</div>
  <div class="abs role-tag">Geschäftsführer</div>

  <svg class="shapes" viewBox="0 0 780 1103" aria-hidden="true">
    <path d="M0,400 Q430,392 780,498 L780,1103 L0,1103Z" fill="#fff"/>
    <path d="M0,412 Q430,404 780,512" fill="none" stroke="#d9a02a" stroke-width="4"/>
    <path d="M0,935 Q420,940 780,1035 L780,1103 L0,1103Z" fill="#4a3a28"/>
    <path d="M0,930 Q420,932 780,1022" fill="none" stroke="#d9a02a" stroke-width="6"/>
  </svg>

  <h1 class="abs headline" style="top:438px">WAS IST IHRE IMMOBILIE WERT?</h1>
  <h2 class="abs subline" style="top:486px"><span>UNSER SERVICE FÜR SIE</span></h2>

  <div class="service" style="left:40px;top:560px">
    <div class="icon"><svg viewBox="0 0 24 24"><path d="M4 5h16v10H10l-5 4v-4H4z" fill="#3a3025"/></svg></div>
    <div><h3>KOSTENLOSE</h3><p>Beratung durch<br>Experten</p></div>
  </div>
  <div class="service" style="left:40px;top:670px">
    <div class="icon"><svg viewBox="0 0 24 24"><path d="M3 10h4v10H3zM9 10l4-7c2 0 2 2 2 3l-1 4h6c1 0 2 1 1.5 2l-2 7c-.3 1-1 1-2 1H9z" fill="#3a3025"/></svg></div>
    <div><h3>KOSTENLOSE</h3><p>Immobilien-<br>bewertung</p></div>
  </div>
  <div class="service" style="left:40px;top:780px">
    <div class="icon"><svg viewBox="0 0 24 24"><path d="M5 11a7 7 0 0 1 12-4l2-2v6h-6l2-2a4.5 4.5 0 0 0-7.5 2zM19 13a7 7 0 0 1-12 4l-2 2v-6h6l-2 2a4.5 4.5 0 0 0 7.5-2z" fill="#3a3025"/></svg></div>
    <div><h3>KOSTENLOS</h3><p>vorhandene Grund-<br>zeichnung aktualisieren</p></div>
  </div>

  <div class="abs col-divider"></div>

  <div class="service" style="left:430px;top:590px">
    <div class="icon"><svg viewBox="0 0 24 24"><rect x="3" y="5" width="18" height="14" fill="none" stroke="#3a3025" stroke-width="2"/><path d="M5 17l5-6 4 4 2-2 3 4z" fill="#d9a02a"/></svg></div>
    <div><h3>KOSTENLOSE</h3><p>3D Grundzeichnung,<br>3D Fotos</p></div>
  </div>
  <div class="service" style="left:430px;top:700px">
    <div class="icon"><svg viewBox="0 0 24 24"><path d="M6 3h9l4 4v14H6z" fill="none" stroke="#3a3025" stroke-width="2"/><path d="M9 11h7M9 14h7M9 17h5" stroke="#d9a02a" stroke-width="2"/></svg></div>
    <div><h3>KOSTENLOSE</h3><p>Erstellung Ihres<br>Energieausweises</p></div>
  </div>
  <div class="service" style="left:430px;top:810px">
    <div class="icon"><svg viewBox="0 0 24 24"><rect x="9" y="8" width="6" height="8" rx="1" fill="#3a3025"/><path d="M9 9L5 5M15 9l4-4M9 15l-4 4M15 15l4 4" stroke="#3a3025" stroke-width="2"/><circle cx="5" cy="5" r="2" fill="#d9a02a"/><circle cx="19" cy="5" r="2" fill="#d9a02a"/><circle cx="5" cy="19" r="2" fill="#d9a02a"/><circle cx="19" cy="19" r="2" fill="#d9a02a"/></svg></div>
    <div><h3>KOSTENLOSE</h3><p>Drohnenaufnahmen<br>Ihrer Immobilien</p></div>
  </div>

  <div class="contact" style="left:40px;top:982px">
    <svg viewBox="0 0 24 24"><circle cx="12" cy="12" r="11" fill="none" stroke="#fff" stroke-width="2"/><path d="M12 6a4 4 0 0 1 4 4c0 3-4 8-4 8s-4-5-4-8a4 4 0 0 1 4-4z" fill="#fff"/></svg>
    <div><b>Brenkholt &amp; Partner Harlstedt</b><br>31847 Harlstedt-Lindenweg 12</div>
  </div>
  <div class="contact" style="left:300px;top:1008px">
    <svg viewBox="0 0 24 24"><circle cx="12" cy="12" r="11" fill="none" stroke="#fff" stroke-width="2"/><path d="M8 6l3 3-1.5 2a7 7 0 0 0 3.5 3.5l2-1.5 3 3-2 2C10 18 6 14 6 8z" fill="#fff"/></svg>
    <div><b>Telefon Harlstedt:</b><br>+49 (0) 5555 30 80</div>
  </div>
  <div class="contact" style="left:530px;top:1044px">
    <svg viewBox="0 0 24 24"><circle cx="12" cy="12" r="11" fill="none" stroke="#fff" stroke-width="2"/><rect x="6" y="8" width="12" height="8" fill="#fff"/><path d="M6 8l6 5 6-5" fill="none" stroke="#4a3a28" stroke-width="1.5"/></svg>
    <div><b>E-Mail:</b><br>kontakt@brenkholt-immobilien.de</div>
  </div>
  <div class="abs footer-url" style="left:270px;top:1068px">www.brenkholt-immobilien.de</div>
</section>

<section class="flyer flyer--back">
  <div class="abs street" role="img" aria-label="Foto einer Altbaustraße mit Bäumen und parkenden Autos"></div>
  <div class="abs phone-tag"><span class="dot"><svg viewBox="0 0 24 24"><path d="M6 3l4 4-2 3a10 10 0 0 0 6 6l3-2 4 4-3 3C10 21 3 14 3 6z" fill="#fff"/></svg></span>0800 555 210 930</div>

  <svg class="shapes" viewBox="0 0 780 1103" aria-hidden="true">
    <path d="M0,370 Q390,335 780,370 L780,495 Q420,500 0,550Z" fill="#4a3a28"/>
    <path d="M0,370 Q390,335 780,370" fill="none" stroke="#d9a02a" stroke-width="5"/>
    <path d="M0,555 Q420,505 780,502" fill="none" stroke="#d9a02a" stroke-width="5"/>
    <path d="M0,935 Q420,940 780,1035 L780,1103 L0,1103Z" fill="#4a3a28"/>
    <path d="M0,930 Q420,932 780,1022" fill="none" stroke="#d9a02a" stroke-width="6"/>
  </svg>

  <h1 class="abs band-title">TIPPGEBERPRÄMIE</h1>
  <h2 class="abs band-sub">— BRENKHOLT &amp; PARTNER IMMOBILIEN —</h2>

  <div class="abs tip-text">
    <p><strong>So einfach</strong> verdienen Sie sich Ihre Tippprämie: wenn Sie Kenntnis vom beabsichtigten Verkauf einer Immobilie haben, dann setzen Sie sich mit uns in Verbindung.</p>
    <p>Wir belohnen Ihren Tipp – wenn er zu einem Verkaufsabschluss durch uns führt – mit 10 Prozent der an uns gezahlten Netto-Vermittlungsprovision (ohne MwSt.). Dies gilt auch für Eigentümer, die uns Ihre Immobilie zum Verkauf geben.</p>
    <p><strong>Voraussetzungen für die Zahlung einer Tippgeber-Prämie sind:</strong></p>
    <ul class="tip-list">
      <li>Die Brenkholt &amp; Partner Immobilien kennt das angebotene Objekt noch nicht.</li>
      <li>Das Objekt wird nicht bereits im Internet von dritter Seite beworben.</li>
      <li>Die Brenkholt &amp; Partner Immobilien erhält die Erlaubnis zur Vermarktung der Immobilie.</li>
      <li>Es kommt zu einem durch die Brenkholt &amp; Partner Immobilien vermittelten Verkauf.</li>
      <li>Sie erhalten Ihre Tippprämie unmittelbar nach Zahlung der Courtage an uns auf ein von Ihnen genanntes Konto überwiesen!</li>
    </ul>
  </div>

  <div class="contact" style="left:40px;top:982px">
    <svg viewBox="0 0 24 24"><circle cx="12" cy="12" r="11" fill="none" stroke="#fff" stroke-width="2"/><path d="M12 6a4 4 0 0 1 4 4c0 3-4 8-4 8s-4-5-4-8a4 4 0 0 1 4-4z" fill="#fff"/></svg>
    <div><b>Brenkholt &amp; Partner Harlstedt</b><br>31847 Harlstedt-Lindenweg 12</div>
  </div>
  <div class="contact" style="left:300px;top:1008px">
    <svg viewBox="0 0 24 24"><circle cx="12" cy="12" r="11" fill="none" stroke="#fff" stroke-width="2"/><path d="M8 6l3 3-1.5 2a7 7 0 0 0 3.5 3.5l2-1.5 3 3-2 2C10 18 6 14 6 8z" fill="#fff"/></svg>
    <div><b>Telefon Harlstedt:</b><br>+49 (0) 5555 30 80</div>
  </div>
  <div class="contact" style="left:530px;top:1044px">
    <svg viewBox="0 0 24 24"><circle cx="12" cy="12" r="11" fill="none" stroke="#fff" stroke-width="2"/><rect x="6" y="8" width="12" height="8" fill="#fff"/><path d="M6 8l6 5 6-5" fill="none" stroke="#4a3a28" stroke-width="1.5"/></svg>
    <div><b>E-Mail:</b><br>kontakt@brenkholt-immobilien.de</div>
  </div>
  <div class="abs footer-url" style="left:270px;top:1068px">www.brenkholt-immobilien.de</div>
</section>

</body>
</html>
```